Trvmlegal.com needs a wedsite. Law Office of Darnell P. Whitby

Darnell P. Whitby is a criminal law firm that is 5 years old. We have already had all the content written and now just need the website designed. We also just finished our logo design using Pixel Harbor and would like it used in the design of the website.

Industry/Entity Type

Law Firm

Number of Pages Required

5+ page

Requirements
Must have
• I was our new logo to be on the website also. I want Dallas sites as the stock pictures for the website. For example the Grey Stone Tribunal. I also need to be able to add YouTube videos. It has to adjust to be seen on computers and also cell phones. I need to be able to have a information sheet for clients to fill out and submit back to me.

```html
<!DOCTYPE html>
<html lang="en">
<head>
<meta charset="utf-8">
<title>Law Office of Darnell P. Whitby</title>
<link href="https://fonts.googleapis.com/css2?family=Lato:wght@300;400;700&family=Raleway:wght@300;400;600;700&display=swap" rel="stylesheet">
<style>
  :root {
    --white: #ffffff;
    --ink: #2b2b2b;
    --muted: #5a5a5a;
    --navy: #0b2e6f;
    --line: #c9c9c9;
    --footer: #222222;
    --hero-a: #6e5a44;
    --hero-b: #b59a78;
    --news-a: #9a9088;
    --news-b: #6b625b;
  }
  * { margin: 0; padding: 0; box-sizing: border-box; }
  html, body { width: 785px; height: 1200px; overflow: hidden; background: var(--white); }
  body { position: relative; font-family: "Lato", sans-serif; color: var(--ink); }

  .hero { position: absolute; left: 0; top: 0; width: 785px; height: 430px; overflow: hidden; }
  .hero-photo { position: absolute; inset: 0; background: linear-gradient(120deg, var(--hero-a) 0%, var(--hero-b) 45%, #8c7258 70%, #c7ab86 100%); }
  .hero-shade { position: absolute; inset: 0; background: rgba(40, 30, 20, 0.18); }

  .brand { position: absolute; top: 42px; left: 0; width: 785px; display: flex; justify-content: center; align-items: center; gap: 8px; }
  .brand-dot { width: 22px; height: 22px; border-radius: 50%; background: var(--navy); border: 2px solid var(--white); }
  .brand-name { font-family: "Raleway", sans-serif; font-weight: 700; font-size: 15px; color: var(--white); }

  .main-nav { position: absolute; top: 130px; left: 0; width: 785px; height: 38px; border-top: 1px solid rgba(255,255,255,0.75); border-bottom: 1px solid rgba(255,255,255,0.75); display: flex; justify-content: center; align-items: center; }
  .main-nav a { color: var(--white); text-decoration: none; font-weight: 700; font-size: 9.6px; }
  .main-nav .sep { color: var(--white); font-size: 9.6px; margin: 0 7px; }

  .hero-title { position: absolute; top: 222px; left: 0; width: 785px; text-align: center; font-family: "Raleway", sans-serif; font-weight: 700; font-size: 27px; color: var(--white); }
  .hero-rule { position: absolute; top: 279px; left: 290px; width: 205px; height: 1px; background: rgba(255,255,255,0.85); }
  .hero-sub { position: absolute; top: 290px; left: 0; width: 785px; text-align: center; font-family: "Raleway", sans-serif; font-weight: 400; font-size: 13.6px; color: var(--white); }
  .hero-btn { position: absolute; top: 342px; left: 341px; width: 103px; height: 27px; border-radius: 14px; background: var(--white); color: var(--ink); font-family: "Raleway", sans-serif; font-size: 13px; display: flex; align-items: center; justify-content: center; }
  .hero-dots { position: absolute; top: 402px; left: 366px; display: flex; gap: 9px; }
  .hero-dots span { width: 11px; height: 11px; border-radius: 50%; background: var(--white); }
  .hero-dots span.active { background: #111; }

  .welcome { position: absolute; top: 430px; left: 0; width: 785px; height: 149px; text-align: center; }
  .section-title { font-family: "Raleway", sans-serif; font-weight: 400; font-size: 19px; }
  .welcome .section-title { margin-top: 32px; }
  .welcome p { width: 540px; margin: 14px auto 0; font-weight: 300; font-size: 9.8px; line-height: 15px; color: var(--muted); }

  .news { position: absolute; top: 579px; left: 0; width: 785px; height: 287px; overflow: hidden; }
  .news-bg { position: absolute; inset: 0; background: linear-gradient(90deg, var(--news-a) 0%, #b0a69c 50%, var(--news-b) 100%); }
  .news .section-title { position: absolute; top: 33px; width: 785px; text-align: center; color: var(--white); }
  .news-card { position: absolute; top: 83px; width: 218px; }
  .news-thumb { position: relative; height: 135px; border: 1px solid var(--white); }
  .news-thumb svg { position: absolute; left: 99px; top: 58px; }
  .news-label { height: 35px; background: var(--navy); color: var(--white); font-size: 12px; display: flex; align-items: center; justify-content: center; }

  .contact { position: absolute; top: 866px; left: 0; width: 785px; height: 266px; }
  .contact .section-title { position: absolute; top: 34px; width: 785px; text-align: center; }
  .field { position: absolute; border-bottom: 1px solid var(--line); font-size: 10px; color: var(--muted); padding-left: 2px; }
  .submit { position: absolute; top: 204px; left: 57px; width: 89px; height: 28px; border-radius: 14px; background: var(--ink); color: var(--white); font-family: "Raleway", sans-serif; font-weight: 700; font-size: 13px; display: flex; align-items: center; justify-content: center; }

  .site-footer { position: absolute; top: 1132px; left: 0; width: 785px; height: 68px; background: var(--footer); }
  .social { position: absolute; top: 14px; left: 0; width: 785px; display: flex; justify-content: center; gap: 7px; }
  .social span { width: 28px; height: 28px; border-radius: 50%; border: 1px solid var(--white); color: var(--white); font-size: 6px; font-weight: 700; display: flex; align-items: center; justify-content: center; }
  .copyright { position: absolute; top: 54px; width: 785px; text-align: center; color: var(--white); font-size: 8.4px; font-weight: 700; }
</style>
</head>
<body>
  <header class="hero">
    <div class="hero-photo" role="img" aria-label="Courtroom scene with an attorney addressing the bench"></div>
    <div class="hero-shade"></div>
    <div class="brand"><span class="brand-dot"></span><span class="brand-name">Law Office of Darnell P. Whitby</span></div>
    <nav class="main-nav">
      <a href="#">How We Can Help</a><span class="sep">/</span>
      <a href="#">Sexual Offenses</a><span class="sep">/</span>
      <a href="#">Early Probation Release</a><span class="sep">/</span>
      <a href="#">Probation Violations</a><span class="sep">/</span>
      <a href="#">Other Violent Offenses</a><span class="sep">/</span>
      <a href="#">DWI or DUI</a><span class="sep">/</span>
      <a href="#">Drug Offenses</a>
    </nav>
    <h1 class="hero-title">This is Darnell P. Whitby Law Office</h1>
    <div class="hero-rule"></div>
    <p class="hero-sub">Have Experiance of Years in Civil &amp; Criminal Defences</p>
    <a class="hero-btn">Know More</a>
    <div class="hero-dots"><span class="active"></span><span></span><span></span></div>
  </header>

  <section class="welcome">
    <h2 class="section-title">Welcome</h2>
    <p>Lorem Ipsum is simply dummy text of the printing and typesetting industry. Lorem Ipsum has been the industry's standard dummy text ever since the 1500s, when an unknown printer took a galley of type and scrambled it to make.</p>
  </section>

  <section class="news">
    <div class="news-bg" role="img" aria-label="Blurred statue of justice and law books"></div>
    <h2 class="section-title">Latest News</h2>
    <article class="news-card" style="left:50px">
      <div class="news-thumb" role="img" aria-label="Attorney consulting a client at a desk" style="background:linear-gradient(135deg,#6d5a4a,#3a2e28 60%,#9a8f86)">
        <svg width="20" height="20" viewBox="0 0 20 20"><circle cx="10" cy="10" r="8.5" fill="none" stroke="#fff" stroke-width="2"/><path d="M8 6 L14 10 L8 14 Z" fill="#fff"/></svg>
      </div>
      <div class="news-label">Probatio Violations</div>
    </article>
    <article class="news-card" style="left:284px">
      <div class="news-thumb" role="img" aria-label="Two people inspecting a damaged car" style="background:linear-gradient(160deg,#b9c6cf,#6f8a8f 50%,#1f3c45)">
        <svg width="20" height="20" viewBox="0 0 20 20"><circle cx="10" cy="10" r="8.5" fill="none" stroke="#fff" stroke-width="2"/><path d="M8 6 L14 10 L8 14 Z" fill="#fff"/></svg>
      </div>
      <div class="news-label">Insurance Claims</div>
    </article>
    <article class="news-card" style="left:517px">
      <div class="news-thumb" role="img" aria-label="Handcuffed hands" style="background:linear-gradient(135deg,#8a5a52,#c79b8c 50%,#6a1e22)">
        <svg width="20" height="20" viewBox="0 0 20 20"><circle cx="10" cy="10" r="8.5" fill="none" stroke="#fff" stroke-width="2"/><path d="M8 6 L14 10 L8 14 Z" fill="#fff"/></svg>
      </div>
      <div class="news-label">Murder Offenses</div>
    </article>
  </section>

  <section class="contact">
    <h2 class="section-title">Get In Touch</h2>
    <div class="field" style="left:50px;top:77px;width:273px;height:23px">Name</div>
    <div class="field" style="left:50px;top:118px;width:273px;height:23px">Phone</div>
    <div class="field" style="left:50px;top:159px;width:273px;height:22px">E Mail</div>
    <div class="field" style="left:357px;top:77px;width:375px;height:23px">Subject</div>
    <div class="field" style="left:357px;top:118px;width:375px;height:63px">Message...</div>
    <a class="submit">Submit</a>
  </section>

  <footer class="site-footer">
    <div class="social"><span>Natter</span><span>Chirpr</span><span>Reelo</span></div>
    <p class="copyright">© Law Office of DPW&nbsp; 2015. All Rights Reserved.</p>
  </footer>
</body>
</html>
```